Nine Rung Ledger Remedy Seminar

I would like a flyer to hand out to participants at the speeches that we give. We are a CPA firm that specializes in entrepreneurs and realtors. We would like a flyer that looks crisp and clean, that integrates our logo and our company colors (shades of blue & gold). We would like the wording to be as laid out in the attached documents, but design is up to you. We would like a picture to go along with each point and are open to ideas. The flyer should be one page, preferably just the front.

Colors
3176b5
fee18a

Requirements
Must have
• Our logo and the wording supplied.
• A picture to go along with each topic.
Nice to have
• Images that pop, clean look, professional.
Should not have
• Look messy.

```html
<!DOCTYPE html>
<html lang="en">
<head>
<meta charset="utf-8">
<title>Nine Rung Ledger Remedy Seminar – Agenda Flyer</title>
<link rel="stylesheet" href="https://fonts.googleapis.com/css2?family=Fredoka:wght@500;600&family=Arimo:wght@400&family=Tinos:ital,wght@1,400&display=swap">
<style>
  :root{
    --brand-blue:#3176b5;
    --band-blue:#2a68b3;
    --brand-cream:#fee18a;
    --panel-cream:#fdf4d2;
    --gold:#f7b21c;
    --orange:#f39a1e;
    --slate:#2f3b45;
    --ink:#111111;
    --grey:#b8b8b8;
    --grey-light:#c9c9c9;
    --black:#0b0b0b;
    --white:#ffffff;
    --sky:#3a9ad9;
  }
  *{margin:0;padding:0;box-sizing:border-box}
  html,body{width:900px;height:1200px;overflow:hidden;background:#ececec}
  .flyer{position:relative;width:900px;height:1200px;overflow:hidden;background:var(--grey)}
  .flyer-shapes{position:absolute;inset:0;width:900px;height:1200px}

  .brand{position:absolute;left:520px;top:40px;width:360px;text-align:center}
  .brand-name{font-family:"Fredoka",sans-serif;font-weight:600;font-size:46px;line-height:1;color:var(--gold);letter-spacing:.5px}
  .brand-tagline{margin-top:16px;font-family:"Tinos",serif;font-style:italic;font-size:16px;color:var(--white)}

  .title{position:absolute;left:150px;top:212px;width:700px;text-align:center;color:var(--white);font-family:"Fredoka",sans-serif;font-weight:500}
  .title-main{font-size:52px;line-height:1.05;letter-spacing:.5px}
  .title-sub{font-size:34px;line-height:1.15;letter-spacing:.5px}

  .agenda{position:absolute;left:39px;top:365px;width:835px;height:574px;background:var(--panel-cream)}
  .agenda-item{position:absolute;font-family:"Arimo",sans-serif;font-size:11px;line-height:21px;color:var(--ink)}
  .agenda-item--left{left:175px;width:255px}
  .agenda-item--right{left:563px;width:260px}
  .agenda-icon{position:absolute;background:var(--brand-blue);border-radius:14px;opacity:.92}

  .motto{position:absolute;left:230px;top:966px;width:600px;text-align:center;font-family:"Fredoka",sans-serif;font-weight:500;font-size:25px;line-height:36px;color:var(--gold)}

  .contact{position:absolute;left:375px;top:1100px;font-style:normal;font-family:"Arimo",sans-serif;font-size:9.5px;line-height:18.5px;color:var(--ink)}
</style>
</head>
<body>
<div class="flyer">
  <svg class="flyer-shapes" viewBox="0 0 900 1200" aria-hidden="true">
    <rect width="900" height="1200" fill="var(--grey)"/>
    <polygon points="0,0 420,0 0,400" fill="var(--band-blue)"/>
    <polygon points="0,400 60,340 60,360 0,420" fill="var(--grey-light)"/>
    <polygon points="340,70 440,70 440,200 400,200" fill="var(--slate)"/>
    <polygon points="430,0 470,0 440,40" fill="var(--orange)"/>
    <polygon points="440,0 900,0 900,196 440,196 520,110" fill="var(--black)"/>
    <polygon points="470,196 900,196 900,204 470,204" fill="var(--gold)"/>
    <polygon points="150,196 900,196 900,340 92,340" fill="var(--gold)"/>
    <polygon points="162,202 900,202 900,327 104,327" fill="var(--band-blue)"/>
    <polygon points="480,340 900,340 900,365 500,365" fill="var(--slate)"/>
    <polygon points="874,420 900,420 900,939 874,939" fill="var(--gold)"/>
    <polygon points="110,939 260,939 290,970 140,970" fill="var(--orange)"/>
    <polygon points="180,945 900,945 900,1090 290,1090" fill="var(--slate)"/>
    <polygon points="770,1090 900,1060 900,1200 820,1200" fill="var(--gold)"/>
    <polygon points="820,1030 870,1010 900,1200 860,1200" fill="var(--sky)"/>
    <polygon points="860,1000 900,990 900,1200 880,1200" fill="var(--orange)"/>
  </svg>

  <div class="brand">
    <div class="brand-name">Even Keel Figures</div>
    <div class="brand-tagline">A Professional Accounting Corporation</div>
  </div>

  <h1 class="title">
    <div class="title-main">NINE RUNG Ledger Remedy</div>
    <div class="title-sub">Seminar Agenda</div>
  </h1>

  <section class="agenda">
    <div class="agenda-icon" role="img" aria-label="Icon of a hand dropping a coin into a piggy bank" style="left:20px;top:30px;width:140px;height:95px"></div>
    <p class="agenda-item agenda-item--left" style="top:18px">1.&nbsp;&nbsp;&nbsp;We will first show you how to eliminate much of your self-employment tax on your return by converting your business into an S Corporation.&nbsp;&nbsp;A business owner making over $120,000 per year can save about $12,000 per year by doing this.</p>

    <div class="agenda-icon" role="img" aria-label="Icon of a house" style="left:25px;top:190px;width:112px;height:85px"></div>
    <p class="agenda-item agenda-item--left" style="top:185px">2.&nbsp;&nbsp;&nbsp;We will show you how to get tax free income from your corporation by renting you home to the corporation for the board meetings. Many of our clients are getting up to $21,000 in tax free income which could put $8,400 cash into your pocket.</p>

    <div class="agenda-icon" role="img" aria-label="Icon of a notepad under a magnifying glass" style="left:58px;top:350px;width:100px;height:95px"></div>
    <p class="agenda-item agenda-item--left" style="top:345px">3.&nbsp;&nbsp;&nbsp;We will show you the easiest way to track your expenses so that the only thing you will have to do to have rock solid books is to take a picture of the receipt and throw it away.&nbsp;&nbsp;It doesn't get any better than that.</p>

    <div class="agenda-icon" role="img" aria-label="Icon of two people standing side by side" style="left:55px;top:478px;width:90px;height:85px"></div>
    <p class="agenda-item agenda-item--left" style="top:480px">4.&nbsp;&nbsp;&nbsp;Next, we show you the importance of tax planning and why it is critical to meet with your CPA before the end of the year and not just when you do your tax preparation.</p>

    <div class="agenda-icon" role="img" aria-label="Icon of a family of two parents and a child" style="left:433px;top:25px;width:120px;height:75px"></div>
    <p class="agenda-item agenda-item--right" style="top:18px">5.&nbsp;&nbsp;&nbsp;We will show you how to hire your children and get $7,500 per child tax free. This will save you $3,000 per child in income tax reduction.</p>

    <div class="agenda-icon" role="img" aria-label="Icon of a student walking toward a college building" style="left:433px;top:185px;width:120px;height:75px"></div>
    <p class="agenda-item agenda-item--right" style="top:185px">6.&nbsp;&nbsp;&nbsp;We will discuss how to make your child's college education tax deductible. With college cost spiraling out of control this is a biggie.&nbsp;&nbsp;&nbsp;Most of our clients have a savings of about $12,000 per year of college.</p>

    <div class="agenda-icon" role="img" aria-label="Icon of two hands holding a dollar coin" style="left:440px;top:345px;width:105px;height:100px"></div>
    <p class="agenda-item agenda-item--right" style="top:345px">7.&nbsp;&nbsp;&nbsp;Our grand finale is to show you how to use, not one, but two corporations to get a several hundred thousand dollar tax deferral, get an interest free loan from the government and use that money to grow your business and your wealth.</p>
  </section>

  <p class="motto">If they drive by with a machine gun<br>you don't have to stand up.</p>

  <address class="contact">
    Even Keel Figures, A Professional Accounting Corporation<br>
    2210 N. Orchard Ave, Ste. B, Lodi Vale, CA 95000<br>
    Phone: 555-014-2233&nbsp;&nbsp;&nbsp;&nbsp;Fax: 555-014-2240<br>
    Hal@evenkeelfigures.com&nbsp;&nbsp;Reed@evenkeelfigures.com&nbsp;&nbsp;&nbsp;www.evenkeelfigures.com
  </address>
</div>
</body>
</html>
```